Lumen Haulwise

WHY: So we are looking for a clean blue/modern/ mobile friendly website to be able compete with our rival, which is bellhops.comWHO: Our company is based out Atlanta,GA. The Company named is called "Lumen Haulwise" and we are Professional staffing Agency that trained our employees for Household Industry related tasks such as Moving Furniture, Packers Household Boxes , Velmora Furniture Installers, Mounting TV and etc.WHAT: Our Main Function is we need to be able to pre-qualified lead/schedule them based on availability /Book our client online on Quindex in order to help our client solve and their problem faster than the traditional 20 min phone call. We need an :Pre-Survey Form /Basic Contact Form Example Below...Desired Button Placement: Should be In the Center or Right Corner. * Q1. What would you like help with? (multi-Choice A to D?* Q2. What are you packing or unpacking* Q3. How many boxes would you like packed or unpacked?* Q4.In Additional to packing or unpacking, do you need any other service>* Q5. Would you like to add photos of the primary item you need packed on..* Q6. When would you like the packing specialist?* Q7. WHat time work best for your schedule?* Q8.Anything else the packing specialist should know? * Q8. Zip Code * Q9. Name* Q10. Email (Privacy Disclaimer)* Q12. Number * Q13. Customer Credit Card InfoWHEN: we looking to be done submit all of our revision request and the project done before New Year, Jan.1

Target Market(s)

Womans: Between 25yr to +55 Womans, Affluence,

Industry/Entity Type

Moving

Number of Pages Required

2 page

Font styles to use
Sans Serif

Colors

Designer to choose colors to be used in the design.

Requirements
Must have
• Service Option Category
• Packers/Installer/ Rental Trucks Assistant
• How it Work Session
• 1.Pick a Service
• 2.Book A Time
• 3.Secured A Payment
Nice to have
• Our Main Function is we need to be able to pre-qualified lead/schedule them based on availability /Book our client online on Quindex in order to help our client solve and their problem faster than the traditional 20 min phone call.
• We need an :Pre-Survey Form /Basic Contact Form Example Below...
• Desired Button Placement: Should be In the Center or Right Corner.
• * Q1. What would you like help with? (multi-Choice A to D?
• * Q2. What are you packing or unpacking
• * Q3. How many boxes would you like packed or unpacked?
• * Q4.In Additional to packing or unpacking, do you need any other service>
• * Q5. Would you like to add photos of the primary item you need packed on..
• * Q6. When would you like the packing specialist?
• * Q7. WHat time work best for your schedule?
• * Q8.Anything else the packing specialist should know?
• * Q8. Zip Code
• * Q9. Name
• * Q10. Email (Privacy Disclaimer)
• * Q12. Number
• * Q13. Customer Credit Card Info
Should not have
• we are not interesting for an Basic Template Design /generic Truck photo stock/ traditional moving company website).

```html
<!DOCTYPE html>
<html lang="en">
<head>
<meta charset="utf-8">
<title>Lumen Haulwise</title>
<link href="https://fonts.googleapis.com/css2?family=Montserrat:wght@400;600;700;800&family=Open+Sans:wght@400;600&display=swap" rel="stylesheet">
<style>
:root{
  --teal:#2bbfcf;
  --teal-dark:#1596a8;
  --teal-light:#7fe0e8;
  --ink:#1c1c1c;
  --black:#0e0e0e;
  --panel:#1d2a30;
  --white:#ffffff;
  --grey:#6b6b6b;
  --line:#d7d7d7;
}
*{box-sizing:border-box;margin:0;padding:0}
html,body{width:1200px;height:2792px;overflow:hidden}
body{font-family:"Open Sans",Arial,sans-serif;color:var(--ink);background:var(--white);position:relative}
.abs{position:absolute}
.topbar{left:0;top:0;width:1200px;height:24px;background:var(--black);color:var(--white);font:600 10px "Montserrat",sans-serif;letter-spacing:1px;text-align:center;line-height:24px}
.hero{left:0;top:24px;width:1200px;height:760px}
.brand{left:150px;top:44px;font:800 34px "Montserrat",sans-serif;color:var(--white)}
.menu{left:1000px;top:50px}
.crate{left:210px;top:150px;width:330px;height:260px;border-radius:14px;background:linear-gradient(160deg,#f7c477,#d98a3a)}
.hero-title{left:160px;top:330px;font:800 34px/1.15 "Montserrat",sans-serif;color:var(--ink);text-shadow:0 0 0 transparent}
.arrow{top:320px}
.contact{left:680px;top:124px;width:370px;height:360px;background:var(--panel);border:2px solid var(--teal);padding:28px 30px}
.contact h2{font:600 22px "Montserrat",sans-serif;color:var(--white);text-align:center;margin-bottom:18px}
.field{height:32px;border:1px solid #a9c4cb;margin-bottom:12px;color:var(--white);font:600 11px "Montserrat",sans-serif;padding:9px 10px;letter-spacing:.5px}
.field.msg{height:72px}
.submit{height:38px;background:var(--teal);color:var(--white);font:700 13px "Montserrat",sans-serif;text-align:center;line-height:38px;letter-spacing:1px}
.pricing-head{left:0;top:690px;width:1200px;text-align:center}
.pricing-head p{font:700 20px "Montserrat",sans-serif}
.pricing-head h2{font:800 38px "Montserrat",sans-serif;margin-top:2px}
.card{width:215px;height:250px;background:var(--white);border:1px solid var(--line);box-shadow:0 2px 6px rgba(0,0,0,.15);text-align:center;padding:74px 18px 0}
.card h3{font:700 14px/1.2 "Montserrat",sans-serif;margin-bottom:8px}
.card p{font-size:10.5px;line-height:1.35;color:var(--grey);height:66px}
.card .btn{margin:10px auto 0;width:140px;height:26px;background:var(--teal);color:var(--white);font:700 10px/26px "Montserrat",sans-serif}
.pin{left:50%;top:-26px;transform:translateX(-50%)}
.why{left:0;top:1100px;width:1200px;height:520px}
.why-title{left:0;top:1250px;width:1200px;text-align:center;font:800 38px "Montserrat",sans-serif;color:var(--white)}
.perk{top:1315px;width:180px;text-align:center;color:var(--white);font:700 14px/1.25 "Montserrat",sans-serif}
.perk svg{display:block;margin:0 auto 14px}
.factory{left:0;top:1880px;width:1200px;height:330px;background:linear-gradient(#fafafa,#e8e8e8)}
.video-frame{left:300px;top:1690px;width:500px;height:420px;background:var(--teal)}
.video{left:320px;top:1720px;width:500px;height:420px;background:linear-gradient(135deg,#e9ecef,#b9c3c9)}
.how{left:0;top:2180px;width:1200px;height:530px}
.how-title{left:0;top:2255px;width:1200px;text-align:center;font:700 34px "Montserrat",sans-serif;color:var(--white)}
.step{top:2310px;width:260px;text-align:center;color:var(--white)}
.step h3{font:700 18px "Montserrat",sans-serif;margin:14px 0 6px}
.step p{font-size:11px;line-height:1.4;opacity:.9}
.survey{left:490px;top:2565px;width:220px;height:50px;border:2px solid var(--white);color:var(--white);text-align:center;font:700 15px/46px "Montserrat",sans-serif;letter-spacing:1px}
.footer{left:0;top:2710px;width:1200px;height:82px;text-align:center}
.footer p{font-size:12px;color:var(--grey);padding-top:18px}
.socials{display:flex;justify-content:center;gap:12px;margin-top:10px}
.socials span{width:22px;height:22px;border-radius:50%;background:#8a8a8a}
</style>
</head>
<body>

<div class="abs topbar">WE GET PAID TO SWEAT</div>

<svg class="abs hero" viewBox="0 0 1200 760" aria-hidden="true">
  <defs>
    <linearGradient id="heroBg" x1="0" y1="0" x2="1" y2="1">
      <stop offset="0" stop-color="#3fd0dc"/><stop offset="1" stop-color="#159db0"/>
    </linearGradient>
  </defs>
  <polygon points="0,0 1200,0 1200,560 0,760" fill="url(#heroBg)"/>
  <polygon points="0,520 1200,380 1200,560 0,760" fill="#66d9e3" opacity=".5"/>
  <polygon points="0,600 1200,470 1200,560 0,760" fill="#ffffff" opacity=".25"/>
</svg>

<div class="abs brand">Lumen Haulwise</div>
<svg class="abs menu" width="46" height="26" viewBox="0 0 46 26" aria-label="Menu">
  <rect y="0" width="46" height="4" fill="#fff"/><rect y="11" width="46" height="4" fill="#fff"/><rect y="22" width="46" height="4" fill="#fff"/>
</svg>

<div class="abs crate" role="img" aria-label="Illustration of a taped cardboard moving box flying over clouds"></div>
<div class="abs hero-title">BOOK A LOCAL<br>LUMEN HAULWISE<br>ATHLETE</div>

<svg class="abs arrow" style="left:80px" width="40" height="30" viewBox="0 0 40 30" aria-label="Previous"><path d="M38 15H4M16 3L4 15l12 12" stroke="#fff" stroke-width="3" fill="none"/></svg>
<svg class="abs arrow" style="left:1080px" width="40" height="30" viewBox="0 0 40 30" aria-label="Next"><path d="M2 15h34M24 3l12 12-12 12" stroke="#fff" stroke-width="3" fill="none"/></svg>

<form class="abs contact">
  <h2>CONTACT FORM</h2>
  <div class="field">NAME</div>
  <div class="field">EMAIL</div>
  <div class="field">PHONE</div>
  <div class="field msg">MESSAGE</div>
  <div class="submit">SUBMIT</div>
</form>

<div class="abs pricing-head">
  <p>WHAT WE DO LET GET READY TO MOVE</p>
  <h2>PRICING</h2>
</div>

<div class="abs card" style="left:150px;top:820px">
  <svg class="abs pin" width="52" height="62" viewBox="0 0 52 62"><path d="M26 60C12 42 2 34 2 24a24 24 0 0 1 48 0c0 10-10 18-24 36z" fill="#fff" stroke="#333" stroke-width="2"/><rect x="16" y="16" width="20" height="16" fill="none" stroke="var(--teal)" stroke-width="2"/></svg>
  <h3>PACKAGING</h3>
  <p>Careful packing of every room with sturdy boxes, labels and wrap included.</p>
  <div class="btn">BUY NOW</div>
</div>
<div class="abs card" style="left:380px;top:840px">
  <svg class="abs pin" width="52" height="62" viewBox="0 0 52 62"><path d="M26 60C12 42 2 34 2 24a24 24 0 0 1 48 0c0 10-10 18-24 36z" fill="#fff" stroke="#333" stroke-width="2"/><path d="M12 30h18V18H12zM30 22h6l4 5v3H30" fill="none" stroke="var(--teal)" stroke-width="2"/></svg>
  <h3>MOVING<br>RENTAL TRUCK</h3>
  <p>Trained crew loads and unloads your rental truck safely and fast.</p>
  <div class="btn">BUY NOW</div>
</div>
<div class="abs card" style="left:610px;top:820px">
  <svg class="abs pin" width="52" height="62" viewBox="0 0 52 62"><path d="M26 60C12 42 2 34 2 24a24 24 0 0 1 48 0c0 10-10 18-24 36z" fill="#fff" stroke="#333" stroke-width="2"/><rect x="18" y="12" width="16" height="22" fill="none" stroke="var(--teal)" stroke-width="2"/></svg>
  <h3>PODS</h3>
  <p>We fill and empty your storage pod with care on your schedule.</p>
  <div class="btn">BUY NOW</div>
</div>
<div class="abs card" style="left:840px;top:840px">
  <svg class="abs pin" width="52" height="62" viewBox="0 0 52 62"><path d="M26 60C12 42 2 34 2 24a24 24 0 0 1 48 0c0 10-10 18-24 36z" fill="#fff" stroke="#333" stroke-width="2"/><circle cx="26" cy="24" r="9" fill="none" stroke="var(--teal)" stroke-width="2"/></svg>
  <h3>INSTALLATION</h3>
  <p>Furniture assembly and TV mounting done right by skilled pros.</p>
  <div class="btn">BUY NOW</div>
</div>

<svg class="abs why" viewBox="0 0 1200 520" aria-hidden="true">
  <polygon points="0,40 1200,0 1200,440 0,520" fill="var(--black)"/>
  <polygon points="0,40 1200,0 1200,30 0,90" fill="#2a2a2a"/>
  <polygon points="0,470 1200,400 1200,440 0,520" fill="#2a2a2a"/>
</svg>
<div class="abs why-title">WHY US</div>

<div class="abs perk" style="left:180px">
  <svg width="74" height="74" viewBox="0 0 74 74"><circle cx="37" cy="37" r="33" fill="var(--teal)" stroke="#fff" stroke-width="3"/><path d="M26 50V34h6l6-10c3 0 4 2 3 6h9c2 0 3 2 2 4l-3 12c-1 3-2 4-5 4H26" fill="none" stroke="#fff" stroke-width="2.5"/></svg>
  TRUSTED<br>PACKERS
</div>
<div class="abs perk" style="left:400px">
  <svg width="74" height="74" viewBox="0 0 74 74"><circle cx="37" cy="37" r="33" fill="var(--teal)" stroke="#fff" stroke-width="3"/><path d="M25 38l8 8 16-18" fill="none" stroke="#fff" stroke-width="3"/></svg>
  BACKGROUND<br>CHECK
</div>
<div class="abs perk" style="left:620px">
  <svg width="74" height="74" viewBox="0 0 74 74"><circle cx="37" cy="37" r="33" fill="var(--teal)" stroke="#fff" stroke-width="3"/><rect x="23" y="24" width="28" height="26" fill="none" stroke="#fff" stroke-width="2.5"/><path d="M23 32h28M30 20v8M44 20v8" stroke="#fff" stroke-width="2.5"/></svg>
  SAME DAY<br>AVAILABILITY
</div>
<div class="abs perk" style="left:840px">
  <svg width="74" height="74" viewBox="0 0 74 74"><circle cx="37" cy="37" r="33" fill="var(--teal)" stroke="#fff" stroke-width="3"/><path d="M37 20l13 5v10c0 9-6 15-13 18-7-3-13-9-13-18V25z" fill="none" stroke="#fff" stroke-width="2.5"/><path d="M31 37l5 5 8-9" fill="none" stroke="#fff" stroke-width="2.5"/></svg>
  OUR<br>GUARANTEES
</div>

<div class="abs factory" role="img" aria-label="Faint line drawing of a packing production line with boxes on conveyors"></div>
<div class="abs video-frame"></div>
<div class="abs video" role="img" aria-label="Video still of a smiling team member"></div>
<svg class="abs" style="left:535px;top:1895px" width="70" height="70" viewBox="0 0 70 70" aria-label="Play video"><circle cx="35" cy="35" r="33" fill="#111"/><path d="M28 22l20 13-20 13z" fill="#fff"/></svg>

<svg class="abs how" viewBox="0 0 1200 530" aria-hidden="true">
  <defs><linearGradient id="howBg" x1="0" y1="0" x2="0" y2="1"><stop offset="0" stop-color="#33c7d4"/><stop offset="1" stop-color="#1aa5b6"/></linearGradient></defs>
  <polygon points="0,40 1200,0 1200,530 0,530" fill="url(#howBg)"/>
  <path d="M250 170 Q 420 120 520 170 T 800 170 T 950 170" stroke="#fff" stroke-width="2" stroke-dasharray="6 6" fill="none" opacity=".7"/>
</svg>
<div class="abs how-title">HOW IT WORKS</div>

<div class="abs step" style="left:150px">
  <svg width="150" height="110" viewBox="0 0 150 110"><text x="10" y="95" font-family="Montserrat" font-weight="400" font-size="100" fill="none" stroke="#fff" stroke-width="2">1</text><circle cx="95" cy="55" r="32" fill="none" stroke="#fff" stroke-width="2"/><path d="M95 72c-8-10-12-14-12-20a12 12 0 0 1 24 0c0 6-4 10-12 20z" fill="none" stroke="#fff" stroke-width="2"/></svg>
  <h3>Pick a Service</h3>
  <p>Choose packing, moving or install help in a few quick taps.</p>
</div>
<div class="abs step" style="left:470px">
  <svg width="150" height="110" viewBox="0 0 150 110"><text x="5" y="95" font-family="Montserrat" font-weight="400" font-size="100" fill="none" stroke="#fff" stroke-width="2">2</text><circle cx="95" cy="55" r="32" fill="none" stroke="#fff" stroke-width="2"/><path d="M95 38v17l11 8" fill="none" stroke="#fff" stroke-width="2"/></svg>
  <h3>Book A Time</h3>
  <p>Pick a date and time slot that fits your busy schedule.</p>
</div>
<div class="abs step" style="left:790px">
  <svg width="150" height="110" viewBox="0 0 150 110"><text x="5" y="95" font-family="Montserrat" font-weight="400" font-size="100" fill="none" stroke="#fff" stroke-width="2">3</text><circle cx="95" cy="55" r="32" fill="none" stroke="#fff" stroke-width="2"/><rect x="80" y="44" width="30" height="20" fill="none" stroke="#fff" stroke-width="2"/><path d="M80 50h30" stroke="#fff" stroke-width="2"/></svg>
  <h3>Secured A Payment</h3>
  <p>Pay safely online with Quindex and your booking is confirmed.</p>
</div>

<div class="abs survey">PRE-SURVEY</div>

<footer class="abs footer">
  <p>© 2018 Lumen Haulwise. All right reserved. Terms of Use</p>
  <div class="socials"><span></span><span></span><span></span><span></span></div>
</footer>

</body>
</html>
```